Brambleton Chiropractic. We have two locations that we want to advertise on the same card. Kelwin MotionCare campus address: 3815 Tamsey Rd., Suite 240, Flowood, MS 39987. Madison address: 428 Pellham Ct., Building D., Madison, MS 39974. website: www.drbrambleton-example.com. o:(601)555-0147 f:(601)555-0183

Target Market(s)

Health care decision makers: primary care doctors and mothers

Contact Information for Business Card

I have no idea; up for any suggestions and I'd do much better picking from examples versus describing what I'm looking for. We are in a very high end location and would like the cards to look really sharp.

Requirements
Must have
• My name, Marcus L Denbrook, D.C.

```html
<!DOCTYPE html>
<html lang="en">
<head>
<meta charset="utf-8">
<title>Brambleton Chiropractic – Business Card</title>
<link href="https://fonts.googleapis.com/css2?family=Cormorant+Garamond:ital,wght@0,400;0,500;0,600;1,400&display=swap" rel="stylesheet">
<style>
  :root {
    --stage: #2a2c30;
    --card-white: #ffffff;
    --card-black: #0c0c0d;
    --band-grey: #2e2e30;
    --ink: #141414;
    --ink-soft: #3a3a3a;
    --light-text: #e6e6e6;
    --muted-text: #bdbdbd;
    --figure-faint: #e4e4e4;
  }
  * { box-sizing: border-box; margin: 0; padding: 0; }
  html, body { width: 1200px; height: 900px; overflow: hidden; }
  body {
    background: var(--stage);
    font-family: "Cormorant Garamond", Georgia, serif;
    display: flex;
    align-items: center;
    justify-content: center;
    gap: 40px;
  }
  .card {
    position: relative;
    width: 540px;
    height: 309px;
    overflow: hidden;
    box-shadow: 0 10px 30px rgba(0,0,0,.45);
  }

  /* ---------- Front ---------- */
  .card--front { background: var(--card-white); color: var(--ink); }
  .front__faint-figures {
    position: absolute;
    right: 0; top: 0;
    width: 300px; height: 309px;
    background: linear-gradient(160deg, rgba(228,228,228,0) 0%, var(--figure-faint) 55%, rgba(228,228,228,.3) 100%);
  }
  .front__logo-figure {
    position: absolute;
    left: 60px; top: 40px;
    width: 95px; height: 85px;
    background: radial-gradient(ellipse at 50% 40%, #d0d0d0 0%, #f2f2f2 75%, rgba(255,255,255,0) 100%);
  }
  .front__wordmark {
    position: absolute;
    left: 150px; top: 70px;
  }
  .front__name {
    font-weight: 600;
    font-size: 50px;
    line-height: 1;
    letter-spacing: 1px;
    text-transform: uppercase;
  }
  .front__specialty {
    font-weight: 400;
    font-size: 36px;
    line-height: 1.05;
    letter-spacing: 2px;
    text-transform: uppercase;
    margin-left: 4px;
  }
  .front__campus {
    font-style: italic;
    font-size: 17px;
    margin: 4px 0 0 6px;
    color: var(--ink-soft);
  }
  .front__address {
    font-size: 8.5px;
    letter-spacing: .6px;
    text-transform: uppercase;
    margin: 3px 0 0 6px;
    color: var(--ink-soft);
  }

  /* ---------- Back ---------- */
  .card--back { background: var(--card-black); color: var(--light-text); }
  .back__figure {
    position: absolute;
    left: 40px; top: 0;
    width: 260px; height: 215px;
    background: radial-gradient(ellipse at 45% 35%, #2b2b2d 0%, #161617 60%, rgba(12,12,13,0) 100%);
  }
  .back__doctor {
    position: absolute;
    right: 38px; top: 40px;
    text-align: right;
  }
  .back__name {
    font-variant: small-caps;
    font-size: 22px;
    font-weight: 500;
    letter-spacing: 1px;
  }
  .back__rule {
    width: 18px; height: 1.5px;
    background: var(--light-text);
    margin: 10px 0 10px auto;
  }
  .contact-list { list-style: none; }
  .contact-list li {
    display: flex;
    justify-content: flex-end;
    align-items: center;
    gap: 8px;
    font-size: 17px;
    line-height: 1.3;
  }
  .contact-list svg { width: 13px; height: 13px; fill: none; stroke: var(--light-text); stroke-width: 1.6; }
  .back__band {
    position: absolute;
    left: 0; right: 0; bottom: 0;
    height: 90px;
    background: var(--band-grey);
    display: flex;
    justify-content: space-between;
    padding: 14px 38px 0;
    color: var(--muted-text);
    font-size: 13.5px;
    line-height: 1.35;
  }
  .location__title { font-variant: small-caps; letter-spacing: .6px; color: var(--light-text); }
  .location--madison { text-align: right; }
</style>
</head>
<body>

  <section class="card card--front" aria-label="Business card front">
    <div class="front__faint-figures" role="img" aria-label="Faint line drawing of human backs"></div>
    <div class="front__logo-figure" role="img" aria-label="Line drawing of a human back"></div>
    <div class="front__wordmark">
      <h1 class="front__name">Brambleton</h1>
      <p class="front__specialty">Chiropractic</p>
      <p class="front__campus">Kelwin Professional Campus</p>
      <p class="front__address">3815 Tamsey Road, Suite 240 &nbsp;Flowood, MS 39987</p>
    </div>
  </section>

  <section class="card card--back" aria-label="Business card back">
    <div class="back__figure" role="img" aria-label="White line drawing of a human back on black"></div>

    <div class="back__doctor">
      <h2 class="back__name">Marcus L Denbrook, D.C.</h2>
      <div class="back__rule"></div>
      <ul class="contact-list">
        <li>(601) 555-0147
          <svg viewBox="0 0 16 16" aria-hidden="true"><path d="M3 5c0-2 2-3 5-3s5 1 5 3l-2 1-1-2H6L5 6z"/><rect x="4" y="8" width="8" height="6" rx="1"/></svg>
        </li>
        <li>(601) 555-0183
          <svg viewBox="0 0 16 16" aria-hidden="true"><rect x="2" y="6" width="12" height="8" rx="1"/><rect x="5" y="2" width="6" height="4"/><line x1="5" y1="10" x2="11" y2="10"/></svg>
        </li>
        <li>drbrambleton-example.com
          <svg viewBox="0 0 16 16" aria-hidden="true"><circle cx="8" cy="8" r="6"/><ellipse cx="8" cy="8" rx="2.6" ry="6"/><line x1="2" y1="8" x2="14" y2="8"/></svg>
        </li>
      </ul>
    </div>

    <div class="back__band">
      <address class="location">
        <span class="location__title">Kelwin MotionCare campus</span><br>
        3815 Tamsey Rd., Suite 240<br>
        Flowood, MS 39987
      </address>
      <address class="location location--madison">
        <span class="location__title">Madison</span><br>
        428 Pellham Ct., Building D.<br>
        Madison, MS 39974
      </address>
    </div>
  </section>

</body>
</html>
```